Business Card Design and Basic Text Logo

We are looking for a business card design for an e-business company. Our business is the parent company of a few website businesses. The final logo and business card design will communicate a conservative but modern and expansive business

The Logo text is: 57Commerce
We would also like a basic text logo design for 57Commerce. The logo could also fill up the reverse side of the business card.

The colours we would like to use are:
White
Navy
Black

This is the text that will be added to the card:

Dean Calloway
Business Development Manager

Phone: +61 417 586 924
Email: dean.calloway@57commerce.com.au

Industry/Entity Type

Business

Logo Text

57Commerce

Logo styles of interest
Pictorial/Combination Logo
Requirements
Must have
• Modern and attractive design
Nice to have
• communicate a conservative but modern and expansive business
Should not have
• Should be too dull and plan
• But also should be overly colourful

```html
<!DOCTYPE html>
<html lang="en">
<head>
<meta charset="utf-8">
<title>57Commerce – Business Card</title>
<link rel="stylesheet" href="https://fonts.googleapis.com/css2?family=Tinos&family=Carlito&display=swap">
<style>
  :root {
    --paper: #ffffff;
    --navy: #2a2459;
    --brand-navy: #3b2f8f;
    --ink-light: #f4f4f8;
    --edge: #111111;
  }
  html, body {
    margin: 0;
    padding: 0;
    width: 1200px;
    height: 666px;
    overflow: hidden;
    background: var(--paper);
  }
  .card {
    position: relative;
    width: 1200px;
    height: 666px;
    background: var(--paper);
  }
  .brand {
    position: absolute;
    left: 32px;
    top: 150px;
    display: flex;
    align-items: center;
    gap: 16px;
  }
  .brand-mark {
    width: 58px;
    height: 58px;
    border-radius: 50%;
    background: var(--brand-navy);
    flex: none;
  }
  .brand-wordmark {
    margin: 0;
    font-family: "Tinos", "Times New Roman", serif;
    font-weight: 400;
    font-size: 68px;
    line-height: 1;
    letter-spacing: 1px;
    color: var(--brand-navy);
  }
  .contact-panel {
    position: absolute;
    left: 538px;
    top: 0;
    width: 644px;
    height: 656px;
    box-sizing: border-box;
    background: var(--navy);
    border: 1.5px solid var(--edge);
    border-radius: 0 34px 34px 0;
    color: var(--ink-light);
  }
  .person-name {
    position: absolute;
    left: 46px;
    top: 373px;
    margin: 0;
    font-family: "Tinos", "Times New Roman", serif;
    font-weight: 400;
    font-size: 49px;
    line-height: 1;
  }
  .person-role {
    position: absolute;
    left: 48px;
    top: 440px;
    margin: 0;
    font-family: "Tinos", "Times New Roman", serif;
    font-size: 26px;
    line-height: 1;
  }
  .contact-line {
    position: absolute;
    left: 46px;
    margin: 0;
    font-family: "Carlito", "Calibri", sans-serif;
    font-size: 29px;
    line-height: 1;
  }
  .contact-phone { top: 484px; }
  .contact-email { top: 527px; }
</style>
</head>
<body>
  <div class="card">
    <div class="brand">
      <span class="brand-mark" aria-hidden="true"></span>
      <p class="brand-wordmark">57Commerce</p>
    </div>
    <section class="contact-panel">
      <h1 class="person-name">Dean Calloway</h1>
      <p class="person-role">Business Development Manager</p>
      <p class="contact-line contact-phone">Phone: +61 417 586 924</p>
      <p class="contact-line contact-email">Email: dean.calloway@57commerce.com.au</p>
    </section>
  </div>
</body>
</html>
```